Email Signature Gif Animation Design

We are looking for an interactive Email Signature to Standardize around for our growing company.

We are a commerical electrical contractor based out of North Jersey. We have a big corporate client tele and perfer a more professional fresh looking signature with titles and perhaps a suttle animation for effect.

Attached below is our company logo which is to be used prominently in the emai signature. We would consider a "refresh' of our logo design provided it does deviate too much.

We would like the tag Line "The KALV Electric Way" worked into that signature as a option.
Updates

Reviewing designs and am underwhelmed with the creativiity and designs, this is anyones prize!

Target Market(s)

Corporate / Middle Managers

Industry/Entity Type

Electrical Contracting & Engineering

Colors
FFF300
FFF600
FEFA6F
FFFEC7
FFFEE8

Requirements
Must have
• Must have, First & Last Name of Employee, Title of Employee, Office & Cell Phone Number, Email Address
Nice to have
• Gif Animation

```html
<!DOCTYPE html>
<html lang="en">
<head>
<meta charset="UTF-8">
<title>KALV Electric LLC – Email Signature</title>
<link rel="stylesheet" href="https://fonts.googleapis.com/css2?family=Oswald:wght@600&family=Roboto:wght@400;500&family=Roboto+Condensed:wght@700&display=swap">
<style>
  :root{
    --paper:#ffffff;
    --ink:#1a1a1a;
    --muted:#3a3a3a;
    --gold:#e2b91c;
    --yellow:#f5c400;
    --band-dark:#3b3712;
    --dots:#ececec;
  }
  *{margin:0;padding:0;box-sizing:border-box}
  html,body{width:1200px;height:414px;overflow:hidden;background:var(--paper)}
  .signature{position:relative;width:1200px;height:414px;background:var(--paper);font-family:'Roboto',Arial,sans-serif;color:var(--ink);overflow:hidden}
  .texture{position:absolute;right:0;top:0;width:560px;height:414px;
    background:radial-gradient(ellipse at 100% 20%,var(--dots) 0%,rgba(236,236,236,.5) 35%,rgba(255,255,255,0) 70%)}
  .portrait{position:absolute;left:116px;top:29px;width:232px;height:232px;border-radius:50%;
    border:7px solid var(--gold);background:radial-gradient(circle at 50% 40%,#8a6a4a 0%,#4a3a2c 55%,#2a2522 100%)}
  .name{position:absolute;left:0;width:441px;top:262px;text-align:center;font-family:'Oswald',Impact,sans-serif;font-weight:600;font-size:52px;letter-spacing:4px;color:var(--ink);line-height:1.2}
  .title{position:absolute;left:0;width:441px;top:340px;text-align:center;font-size:21px;font-weight:500;color:var(--ink)}
  .divider{position:absolute;left:440px;top:31px;width:3px;height:352px;background:var(--gold)}
  .brand{position:absolute;left:507px;top:176px;font-family:'Roboto Condensed',Arial,sans-serif;font-weight:700;font-size:36px;letter-spacing:1px;color:var(--ink);line-height:1}
  .contact{position:absolute;display:flex;align-items:center;gap:14px;font-size:24px;color:var(--ink)}
  .contact small{font-size:9px;margin-left:5px;color:var(--muted)}
  .icon{width:38px;height:38px;flex:none}
  .email{left:498px;top:250px}
  .web{left:850px;top:250px}
  .phone-home{left:498px;top:308px}
  .phone-office{left:766px;top:315px}
  .tagline-band{position:absolute;right:0;bottom:0;width:400px;height:46px}
  .tagline{position:absolute;right:28px;bottom:9px;font-family:'Roboto Condensed',Arial,sans-serif;font-weight:700;font-size:26px;color:var(--ink)}
</style>
</head>
<body>
<div class="signature">
  <div class="texture"></div>

  <div class="portrait" role="img" aria-label="Portrait photo of the employee"></div>
  <div class="name">DANIEL CARTER</div>
  <div class="title">Marketing Manager</div>

  <div class="divider"></div>

  <div class="brand">KALV ELECTRIC LLC</div>

  <div class="contact email">
    <svg class="icon" viewBox="0 0 38 38"><circle cx="19" cy="19" r="19" fill="var(--yellow)"/><rect x="10" y="12.5" width="18" height="13" rx="1.5" fill="var(--ink)"/><path d="M10.5 13.5 19 20l8.5-6.5" fill="none" stroke="var(--yellow)" stroke-width="1.6"/></svg>
    <span>name@thecompany.com</span>
  </div>
  <div class="contact web">
    <svg class="icon" viewBox="0 0 38 38"><circle cx="19" cy="19" r="19" fill="var(--yellow)"/><g fill="none" stroke="var(--ink)" stroke-width="1.8"><circle cx="19" cy="19" r="9"/><ellipse cx="19" cy="19" rx="4" ry="9"/><path d="M10 19h18M11.5 14h15M11.5 24h15"/></g></svg>
    <span>yourwebaddress.com</span>
  </div>
  <div class="contact phone-home">
    <svg class="icon" viewBox="0 0 38 38"><circle cx="19" cy="19" r="19" fill="var(--yellow)"/><path d="M13.5 10.5l3.5-.5 2 5-2.5 1.8a12 12 0 0 0 5.2 5.2L23.5 19.5l5 2-.5 3.5c-.3 1.4-1.6 2.2-3 2A16 16 0 0 1 11.5 13.5c-.2-1.4.6-2.7 2-3z" fill="var(--ink)"/></svg>
    <span>123 456 7890<small>(Home)</small></span>
  </div>
  <div class="contact phone-office">
    <span>123 456 7890<small>(Office)</small></span>
  </div>

  <svg class="tagline-band" viewBox="0 0 400 46" preserveAspectRatio="none" aria-hidden="true">
    <polygon points="18,0 400,0 400,46 0,46" fill="var(--band-dark)"/>
    <polygon points="40,0 400,0 400,46 22,46" fill="var(--gold)"/>
  </svg>
  <div class="tagline">The KALV Electric Way</div>
</div>
</body>
</html>
```